New Business Card Design Project

I need a design for business cards, i am an electrical business called "Tandor Electrical and Communications" i need the cards to be double sided with the company logo on the back (attached) the front needs to say my company name, web site, email address, telephone number, and ABN number and electrical license number. I am open to different arrangements of the information but would like the background to be incorporating something electrical or something that looks smart. open to all additional ideas also.

The company colours are orange and grey see logo attached.

Business Name: Tandor Electrical and Communications
Website: tandorelectricalandcomms.example.au
Email: brent@tandorelectricalandcomms.example.au
Telephone(mobile): 0481203967
ABN: 71829034618
Lic No: 830472F

Target Market(s)

Business entities, Project Managers, Accounts, Clients

Industry/Entity Type

Electrician

Contact Information for Business Card

I need a design for business cards, i am an electrical business called "Tandor Electrical and Communications" i need the cards to be double sided with the company logo on the back (attached) the front needs to say my company name

Font styles to use
Serif
Sans Serif

Colors
f37122
5c5c5c

Requirements
Must have
• Must have the Logo on the back open to different ways of it being on the back but had in mind to keep it central but again open to other options
Nice to have
• A real modern cool background that is eye catching yet contemporary
Should not have
• No backgrounds of a light bulb or plug or anything like that

```html
<!DOCTYPE html>
<html lang="en">
<head>
<meta charset="utf-8">
<title>Tandor Electrical and Communications – Business Cards</title>
<link rel="stylesheet" href="https://fonts.googleapis.com/css2?family=Arimo:wght@400;700&display=swap">
<style>
  :root {
    --stage: #e9e7e3;
    --card-dark: #5c5c5c;
    --card-darker: #3e3e3e;
    --card-light: #6c6c6c;
    --orange: #f37122;
    --amber: #f6a51e;
    --white: #ffffff;
    --ink: #4a4a4a;
    --logo-white: #f1f1f1;
  }
  * { box-sizing: border-box; margin: 0; padding: 0; }
  html, body { width: 1200px; height: 843px; overflow: hidden; }
  body {
    background: var(--stage);
    font-family: "Arimo", Arial, sans-serif;
    position: relative;
  }
  .card {
    position: absolute;
    width: 620px;
    height: 360px;
    border-radius: 22px;
    overflow: hidden;
    background: linear-gradient(160deg, var(--card-light) 0%, var(--card-dark) 45%, var(--card-darker) 100%);
    box-shadow: 0 10px 28px rgba(0,0,0,0.22);
  }
  .card--back { left: 90px; top: 50px; }
  .card--front { left: 490px; top: 432px; }

  /* back side */
  .back-logo {
    position: absolute;
    left: 0; right: 0; top: 120px;
    text-align: center;
  }
  .brand-name {
    font-family: "Arimo", Arial, sans-serif;
    font-weight: 400;
    color: var(--logo-white);
    letter-spacing: 0.08em;
  }
  .back-logo .brand-name { font-size: 64px; }
  .back-url {
    position: absolute;
    left: 0; right: 0; bottom: 46px;
    text-align: center;
    color: var(--logo-white);
    font-size: 15px;
    letter-spacing: 0.18em;
  }

  /* front side */
  .front-shape { position: absolute; inset: 0; }
  .contact {
    position: absolute;
    left: 30px; top: 60px;
    color: var(--ink);
    font-size: 15px;
    line-height: 1.4;
  }
  .contact__name {
    color: var(--amber);
    font-weight: 700;
    font-size: 22px;
    line-height: 1.2;
    letter-spacing: 0.04em;
  }
  .contact__role { letter-spacing: 0.03em; margin-bottom: 6px; }
  .contact__line { display: flex; align-items: center; gap: 8px; white-space: nowrap; }
  .contact__icon { width: 15px; height: 15px; flex: none; }
  .front-logo {
    position: absolute;
    right: 28px; top: 118px;
    width: 190px;
    text-align: right;
  }
  .front-logo .brand-name {
    font-size: 40px;
    letter-spacing: 0.06em;
    display: block;
    line-height: 1;
  }
  .front-logo__sub {
    display: block;
    margin-top: 8px;
    color: var(--amber);
    font-size: 10px;
    font-weight: 700;
    letter-spacing: 0.04em;
    white-space: nowrap;
  }
</style>
</head>
<body>

  <section class="card card--back" aria-label="Card back">
    <div class="back-logo">
      <span class="brand-name">TANDOR</span>
    </div>
    <p class="back-url">www.tandorelectricalandcomms.example.au</p>
  </section>

  <section class="card card--front" aria-label="Card front">
    <svg class="front-shape" viewBox="0 0 620 360" width="620" height="360" aria-hidden="true">
      <circle cx="40" cy="250" r="340" fill="none" stroke="var(--amber)" stroke-width="3"/>
      <circle cx="40" cy="250" r="330" fill="var(--white)"/>
    </svg>

    <div class="contact">
      <p class="contact__name">DANA WHITFIELD</p>
      <p class="contact__role">CEO/FOUNDER</p>
      <p>ABN: 71829034618</p>
      <p>Lic No: 830472F</p>
      <p class="contact__line">
        <svg class="contact__icon" viewBox="0 0 16 16" aria-hidden="true"><rect x="3.5" y="1" width="9" height="14" rx="1.5" fill="none" stroke="var(--amber)" stroke-width="1.8"/><rect x="6.5" y="12" width="3" height="1.4" fill="var(--amber)"/></svg>
        0481203967
      </p>
      <p class="contact__line">
        <svg class="contact__icon" viewBox="0 0 16 16" aria-hidden="true"><rect x="1" y="3" width="14" height="10" rx="1" fill="var(--amber)"/><path d="M1.5 3.8 8 9 14.5 3.8" fill="none" stroke="var(--white)" stroke-width="1.3"/></svg>
        brent@tandorelectricalandcomms.example.au
      </p>
      <p class="contact__line">
        <svg class="contact__icon" viewBox="0 0 16 16" aria-hidden="true"><circle cx="8" cy="8" r="6.5" fill="none" stroke="var(--amber)" stroke-width="1.6"/><ellipse cx="8" cy="8" rx="2.8" ry="6.5" fill="none" stroke="var(--amber)" stroke-width="1.2"/><path d="M1.5 8h13" stroke="var(--amber)" stroke-width="1.2"/></svg>
        tandorelectricalandcomms.example.au
      </p>
    </div>

    <div class="front-logo">
      <span class="brand-name">TANDOR</span>
      <span class="front-logo__sub">ELECTRICAL &amp; COMMUNICATIONS</span>
    </div>
  </section>

</body>
</html>
```